Commercial real estate Brokerage logo, letterhead and business card design

Boutique Commercial real Estate Brokerage and development company requires logo, letterhead/stationary and business card design. For reference, competitors include Harper Vale Brightwood, Pemberton & Oakhurst, Renwick Galloway and Tamsin which all have designs which evoke strong corporate image.
Updates

The name of the firm is Brantley Real Estate. If you look at my competitors web sites you will see their logos. I am looking for something that has a similar flavor - not the same colors or graphics - just how you feel when you see their logo. 
1. www.hvb-realty.example
2. http://www.tamsinprop.example/en-us
3. http://www.pembertonoakhurst.example/

Industry/Entity Type

Real Estate

```html
<!DOCTYPE html>
<html lang="en">
<head>
<meta charset="utf-8">
<title>Brantley Real Estate – Stationery</title>
<link href="https://fonts.googleapis.com/css2?family=Play&family=PT+Serif&display=swap" rel="stylesheet">
<style>
  :root {
    --navy: #0c2266;
    --green: #76b043;
    --paper: #ffffff;
    --paper-shade: #f1f2f4;
    --ink: #222;
    --canvas: #ffffff;
    --sans: "Play", Arial, sans-serif;
    --serif: "PT Serif", Georgia, serif;
  }
  * { box-sizing: border-box; margin: 0; padding: 0; }
  html, body { width: 1200px; height: 1000px; overflow: hidden; background: var(--canvas); }
  .canvas { position: relative; width: 1200px; height: 1000px; }

  .brand { display: flex; align-items: center; gap: 14px; font-family: var(--sans); color: var(--navy); white-space: nowrap; }
  .brand-square { background: var(--green); flex: none; }
  .brand-name { font-weight: 400; }

  .brand--hero { position: absolute; left: 0; right: 0; top: 100px; justify-content: center; gap: 22px; }
  .brand--hero .brand-square { width: 46px; height: 46px; }
  .brand--hero .brand-name { font-size: 50px; letter-spacing: 1px; }

  .card { position: absolute; width: 360px; height: 200px; box-shadow: 0 1px 4px rgba(0,0,0,.18); }
  .card--front { left: 95px; top: 480px; background: var(--navy); display: flex; align-items: center; justify-content: center; }
  .card--front .brand { color: #fff; }
  .card--front .brand-square { width: 22px; height: 22px; }
  .card--front .brand-name { font-size: 24px; }

  .card--back { left: 95px; top: 720px; background: var(--paper); }
  .card--back .brand { position: absolute; left: 28px; top: 24px; gap: 10px; }
  .card--back .brand-square { width: 16px; height: 16px; }
  .card--back .brand-name { font-size: 18px; }
  .card-holder { position: absolute; left: 104px; top: 74px; font-family: var(--sans); font-size: 17px; color: var(--navy); }
  .card-rule { position: absolute; left: 0; right: 0; top: 108px; height: 3px; background: var(--green); }
  .card-rule--navy { top: 111px; height: 7px; background: var(--navy); }
  .card-contact { position: absolute; left: 104px; top: 132px; font-family: var(--sans); font-size: 10px; line-height: 13px; color: var(--navy); list-style: none; }

  .letterhead { position: absolute; left: 645px; top: 262px; width: 470px; height: 650px; background: linear-gradient(135deg, var(--paper) 40%, var(--paper-shade)); box-shadow: 0 1px 5px rgba(0,0,0,.2); }
  .letterhead .brand { position: absolute; left: 47px; top: 62px; gap: 8px; }
  .letterhead .brand-square { width: 13px; height: 13px; }
  .letterhead .brand-name { font-size: 14px; }
  .letter { position: absolute; left: 47px; top: 116px; width: 310px; font-family: var(--serif); font-size: 8.6px; line-height: 11px; color: var(--ink); }
  .letter-address { margin-bottom: 30px; }
  .letter p { margin-bottom: 11px; }
  .letter-closing { margin-top: 20px; }
  .signature { display: block; width: 150px; height: 42px; margin-top: 6px; background: linear-gradient(90deg, #e6e6e6, #d6d6d6); border-radius: 3px; }
  .letter-footer { position: absolute; left: 47px; right: 68px; top: 612px; display: flex; justify-content: space-between; font-family: var(--serif); font-size: 5.4px; color: var(--ink); list-style: none; }
  .letter-band { position: absolute; left: 0; right: 0; bottom: 12px; height: 4px; background: var(--green); }
  .letter-band--navy { bottom: 0; height: 12px; background: var(--navy); }
</style>
</head>
<body>
<main class="canvas">
  <div class="brand brand--hero">
    <span class="brand-square"></span>
    <span class="brand-name">Brantley Real Estate</span>
  </div>

  <section class="card card--front" aria-label="Business card front">
    <div class="brand"><span class="brand-square"></span><span class="brand-name">Brantley Real Estate</span></div>
  </section>

  <section class="card card--back" aria-label="Business card back">
    <div class="brand"><span class="brand-square"></span><span class="brand-name">Brantley Real Estate</span></div>
    <div class="card-holder">Your Name</div>
    <div class="card-rule"></div>
    <div class="card-rule card-rule--navy"></div>
    <ul class="card-contact">
      <li>1840 Fairmont</li>
      <li>phone: 555.010.5558</li>
      <li>fax 555.010.6547</li>
      <li>e-mail: mymail@brantley.example</li>
    </ul>
  </section>

  <section class="letterhead" aria-label="Letterhead">
    <div class="brand"><span class="brand-square"></span><span class="brand-name">Brantley Real Estate</span></div>
    <div class="letter">
      <div class="letter-address">April 26, 2013<br>1840 N. Alder Blvd.<br>Fairmont, ST 40210</div>
      <p>Dear Ms. Ardell,</p>
      <p>It was a pleasure meeting you briefly at last week's Board of Trade event. It's amazing how small the world does seem sometimes are also considering that we both earned our undergraduate degrees at U. of Larkfield, even overlapping for one year! I suppose we were destined to eventually meet face-to-face. I was fascinated by your synopsis of the history of Corvale Industries over the past, almost half-century. Clearly, your company has a rich corporate heritage and tradition.</p>
      <p>As I was mentioning to you, Northgate Press is a specialty publisher that focuses on corporate publications including annual reports, corporate profiles and corporate histories. We have been in business for over 15 years and during that time have grown from a two-person start-up, to a serious corporate publisher with over 100 employees. We have been contracted by over a dozen Fortune 500 companies to produce both annual and special occasion publications on their behalf.</p>
      <p>I have a strong feeling that what we offer at Northgate might be just the kind of thing you've been looking for to celebrate Corvale's 50th. Please feel free to call me at 555-0148 so that we can discuss this further. If I don't hear from you by the end of next week I will follow up with you and see if we can set up a meeting at your convenience.</p>
      <div class="letter-closing">Yours truly,</div>
      <span class="signature" role="img" aria-label="Handwritten signature of Lena Whitford"></span>
    </div>
    <ul class="letter-footer">
      <li>4120 Harbor Boulevard Fairmont, ST 40278</li>
      <li>www.brantley.example</li>
      <li>Phone: 555.010.2000</li>
      <li>Fax: 555.010.0608</li>
    </ul>
    <div class="letter-band"></div>
    <div class="letter-band letter-band--navy"></div>
  </section>
</main>
</body>
</html>
```